Advertisement Design

I'm looking for a post card sized advertisement piece that I will be dropping off to commercial and residential customers.
On one side I want it promoting carpet cleaning services and on the other side dryer vent cleaning services.
I've uploaded two different layouts of my company logo for you to choice from.
One batch will be printed with my Michigan Number
One batch will be printed with my Tennessee number
Will share contact numbers with the winner so just use a make up number
555-318-4729

```html
<!DOCTYPE html>
<html lang="en">
<head>
<meta charset="utf-8">
<title>Fiber Haven – Carpet Cleaning Postcard</title>
<link rel="stylesheet" href="https://fonts.googleapis.com/css2?family=Montserrat:wght@500;600;800&family=Varela+Round&display=swap">
<style>
  :root {
    --brand-blue: #1e7bc4;
    --deep-blue: #1b58a3;
    --navy: #174a8c;
    --sky: #5cbcf0;
    --ink-grey: #5d6166;
    --seal-dark: #3a3f45;
    --white: #ffffff;
  }
  * { margin: 0; padding: 0; box-sizing: border-box; }
  html, body { width: 1200px; height: 857px; overflow: hidden; background: var(--white); }
  .postcard { position: relative; width: 1200px; height: 857px; overflow: hidden; background: var(--white); font-family: "Montserrat", sans-serif; }
  .backdrop { position: absolute; inset: 0; }
  .brand { position: absolute; left: 70px; top: 148px; display: flex; align-items: center; gap: 14px; }
  .brand-square { width: 34px; height: 34px; background: var(--brand-blue); }
  .brand-name { font-family: "Montserrat", sans-serif; font-weight: 600; font-size: 40px; color: var(--brand-blue); letter-spacing: 1px; }
  .headline { position: absolute; left: 56px; top: 296px; color: var(--white); font-weight: 800; font-size: 63px; line-height: 66px; letter-spacing: 1px; }
  .intro { position: absolute; left: 57px; top: 455px; width: 600px; color: var(--white); font-family: "Varela Round", sans-serif; font-size: 20.5px; line-height: 28.5px; }
  .services { position: absolute; list-style: none; color: var(--white); font-weight: 800; font-size: 24px; line-height: 30px; }
  .services li { display: flex; align-items: flex-start; gap: 12px; }
  .services svg { flex: none; margin-top: 3px; }
  .services-left { left: 54px; top: 589px; }
  .services-left li { margin-bottom: 8px; }
  .services-right { left: 537px; top: 604px; }
  .services-right li { margin-bottom: 8px; }
  .tagline { position: absolute; left: 0; top: 783px; width: 492px; text-align: center; color: var(--deep-blue); font-weight: 600; font-size: 24px; line-height: 31px; }
  .offer { position: absolute; left: 512px; top: 777px; text-align: center; color: var(--sky); font-weight: 500; font-size: 24px; line-height: 30px; }
  .divider { position: absolute; left: 743px; top: 772px; width: 2px; height: 65px; background: var(--white); }
  .call { position: absolute; left: 764px; top: 766px; color: var(--white); font-weight: 800; font-size: 35px; letter-spacing: .5px; }
  .web { position: absolute; left: 796px; top: 813px; display: flex; align-items: center; gap: 8px; color: var(--white); font-weight: 500; font-size: 22px; letter-spacing: .5px; }
</style>
</head>
<body>
<main class="postcard">
  <svg class="backdrop" width="1200" height="857" viewBox="0 0 1200 857">
    <defs>
      <linearGradient id="carpetTone" x1="0" y1="0" x2="0" y2="1">
        <stop offset="0" stop-color="#d9d6d0"/>
        <stop offset="0.3" stop-color="#7fb4bd"/>
        <stop offset="1" stop-color="#2f9db3"/>
      </linearGradient>
      <linearGradient id="rugTone" x1="0" y1="0" x2="1" y2="1">
        <stop offset="0" stop-color="#b9bcc6"/>
        <stop offset="1" stop-color="#eee9df"/>
      </linearGradient>
      <linearGradient id="sofaTone" x1="0" y1="0" x2="1" y2="1">
        <stop offset="0" stop-color="#a89d58"/>
        <stop offset="0.4" stop-color="#4b4d55"/>
        <stop offset="1" stop-color="#3a3b42"/>
      </linearGradient>
      <linearGradient id="creamTone" x1="0" y1="0" x2="1" y2="1">
        <stop offset="0" stop-color="#ede6d8"/>
        <stop offset="1" stop-color="#d8cdb9"/>
      </linearGradient>
    </defs>

    <path d="M514,0 H1200 V560 Q900,560 690,420 Q550,300 514,0 Z" fill="url(#carpetTone)" role="img" aria-label="Photo of a carpet extractor wand cleaning a teal shag rug"/>

    <path d="M0,276 Q250,232 470,268 Q700,330 900,520 Q1050,600 1200,560 V771 H0 Z" fill="var(--brand-blue)"/>
    <path d="M0,268 Q250,224 476,262" fill="none" stroke="var(--ink-grey)" stroke-width="12"/>
    <path d="M980,575 Q1090,610 1200,585" fill="none" stroke="var(--ink-grey)" stroke-width="10"/>

    <path d="M467,750 H1200 V857 H492 Z" fill="var(--navy)"/>

    <circle cx="536" cy="283" r="124" fill="url(#rugTone)" stroke="var(--white)" stroke-width="8" role="img" aria-label="Photo of a gloved technician cleaning a fringed rug"/>
    <circle cx="771" cy="446" r="124" fill="url(#sofaTone)" stroke="var(--white)" stroke-width="8" role="img" aria-label="Photo of upholstery being cleaned with a hand tool"/>
    <circle cx="1050" cy="463" r="124" fill="url(#creamTone)" stroke="var(--white)" stroke-width="8" role="img" aria-label="Photo of a stain being lifted from cream carpet"/>

    <g class="seal" transform="translate(1067,651)">
      <circle r="86" fill="var(--brand-blue)"/>
      <circle r="76" fill="var(--seal-dark)"/>
      <circle r="42" fill="var(--white)" stroke="var(--sky)" stroke-width="3"/>
      <path id="sealArc" d="M-58,0 A58,58 0 0 1 58,0" fill="none"/>
      <path id="sealArcLow" d="M-60,0 A60,60 0 0 0 60,0" fill="none"/>
      <text font-family="Montserrat, sans-serif" font-weight="800" font-size="17" fill="var(--white)" letter-spacing="1"><textPath href="#sealArc" startOffset="50%" text-anchor="middle">SATISFACTION</textPath></text>
      <text font-family="Montserrat, sans-serif" font-weight="800" font-size="17" fill="var(--white)" letter-spacing="1" dy="12"><textPath href="#sealArcLow" startOffset="50%" text-anchor="middle">GUARANTEED</textPath></text>
      <text y="14" text-anchor="middle" font-family="Montserrat, sans-serif" font-weight="800" font-size="30" fill="var(--brand-blue)">100%</text>
      <text y="-16" text-anchor="middle" font-size="12" fill="var(--brand-blue)">★★★</text>
    </g>
  </svg>

  <div class="brand">
    <span class="brand-square"></span>
    <span class="brand-name">FIBER HAVEN</span>
  </div>

  <h1 class="headline">CARPET<br>CLEANING</h1>

  <p class="intro">We have been providing Carpet Cleaning Services for 40 years. With state-of-the-art industrial equipment &amp; out years of experience there is not mush we cannot get clean.</p>

  <ul class="services services-left">
    <li><svg width="24" height="24" viewBox="0 0 24 24"><circle cx="12" cy="12" r="10" fill="none" stroke="#fff" stroke-width="2.5"/><path d="M7 12.5l3.2 3.2L17 9" fill="none" stroke="#fff" stroke-width="2.8"/></svg>RUG CLEANING</li>
    <li><svg width="24" height="24" viewBox="0 0 24 24"><circle cx="12" cy="12" r="10" fill="none" stroke="#fff" stroke-width="2.5"/><path d="M7 12.5l3.2 3.2L17 9" fill="none" stroke="#fff" stroke-width="2.8"/></svg>BLEACH REPAIR</li>
    <li><svg width="24" height="24" viewBox="0 0 24 24"><circle cx="12" cy="12" r="10" fill="none" stroke="#fff" stroke-width="2.5"/><path d="M7 12.5l3.2 3.2L17 9" fill="none" stroke="#fff" stroke-width="2.8"/></svg>UPHOLSTERY CLEANING</li>
    <li><svg width="24" height="24" viewBox="0 0 24 24"><circle cx="12" cy="12" r="10" fill="none" stroke="#fff" stroke-width="2.5"/><path d="M7 12.5l3.2 3.2L17 9" fill="none" stroke="#fff" stroke-width="2.8"/></svg>PET STAIN AND SCENT REMOVAL</li>
  </ul>

  <ul class="services services-right">
    <li><svg width="24" height="24" viewBox="0 0 24 24"><circle cx="12" cy="12" r="10" fill="none" stroke="#fff" stroke-width="2.5"/><path d="M7 12.5l3.2 3.2L17 9" fill="none" stroke="#fff" stroke-width="2.8"/></svg><span>BOAT, RV, PRIVATE PLANE<br>CARPET CLEANING</span></li>
    <li><svg width="24" height="24" viewBox="0 0 24 24"><circle cx="12" cy="12" r="10" fill="none" stroke="#fff" stroke-width="2.5"/><path d="M7 12.5l3.2 3.2L17 9" fill="none" stroke="#fff" stroke-width="2.8"/></svg><span>CORRIDOR &amp; OUTDOOR<br>CARPET CLEANING</span></li>
  </ul>

  <p class="tagline">RESIDENTIAL &amp; COMMERCIAL<br>CLEANING SERVICES</p>
  <p class="offer">GET YOUR FREE<br>QUOTE TODAY !</p>
  <span class="divider"></span>
  <p class="call">CALL&nbsp; (555) 318-4729</p>
  <p class="web">
    <svg width="20" height="20" viewBox="0 0 20 20" fill="none" stroke="#fff" stroke-width="1.6"><circle cx="10" cy="10" r="8"/><ellipse cx="10" cy="10" rx="3.5" ry="8"/><path d="M2 10h16M3.5 6h13M3.5 14h13"/></svg>
    WWW.FIBERHAVEN.COM
  </p>
</main>
</body>
</html>
```